Digital Album Cover - Piano music for wedding ceremonies and receptions

I need cover art for a piano album project that will be distributed to TuneVault, Streamora etc. Covert art required for front of album. At this stage physical CDs will not be printed nor required it is just a digital release.
Artist name: Leon Harwick
Album Title: Timeless Keys for Vows and Banquet Evenings
Volume 3
Sample piano songs are on my wavehollow page
https://tunevault.example/leonharwickkeys/sets/timeless-keys-vol-3
Previous album artwork used from pixel guild competitions winners
https://musicshelf.example/au/artist/leon-harwick/4830192775
Target Market(s)
brides to be
grooms to be
people interested in weddings
people enjoy love songs or easy listening music
Industry/Entity Type
Wedding
Look and feel

```html
<!DOCTYPE html>
<html lang="en">
<head>
<meta charset="utf-8">
<title>Leon Harwick – Timeless Keys Volume 3</title>
<link href="https://fonts.googleapis.com/css2?family=Raleway:wght@500;600;700;800&display=swap" rel="stylesheet">
<style>
  :root {
    --ink: #040404;
    --paper: #ffffff;
    --numeral: rgba(150, 148, 146, 0.78);
    --ring: rgba(150, 150, 150, 0.4);
    --frame: #ffffff;
  }
  html, body {
    margin: 0;
    padding: 0;
    width: 1200px;
    height: 1200px;
    overflow: hidden;
    background: var(--ink);
  }
  .cover {
    position: relative;
    width: 1200px;
    height: 1200px;
    overflow: hidden;
    background: var(--ink);
    font-family: "Raleway", sans-serif;
    color: var(--paper);
  }
  .cover-art {
    position: absolute;
    inset: 0;
  }
  .frame {
    position: absolute;
    left: 60px;
    top: 60px;
    width: 1081px;
    height: 1081px;
    border: 2px solid var(--frame);
    box-sizing: border-box;
  }
  .volume-label {
    position: absolute;
    right: 330px;
    top: 134px;
    margin: 0;
    font-weight: 600;
    font-size: 82px;
    line-height: 1;
    letter-spacing: -1px;
  }
  .artist-name {
    position: absolute;
    left: 194px;
    top: 222px;
    margin: 0;
    font-weight: 700;
    font-size: 74px;
    line-height: 1;
    letter-spacing: 15px;
    white-space: nowrap;
  }
  .album-title {
    position: absolute;
    left: 196px;
    top: 318px;
    margin: 0;
    font-weight: 500;
    font-size: 35px;
    line-height: 48px;
  }
</style>
</head>
<body>
  <div class="cover">
    <svg class="cover-art" width="1200" height="1200" viewBox="0 0 1200 1200">
      <defs>
        <linearGradient id="backdrop-tone" x1="0.2" y1="0" x2="0" y2="1">
          <stop offset="0" stop-color="#030303"/>
          <stop offset="0.55" stop-color="#070707"/>
          <stop offset="0.78" stop-color="#1a1918"/>
          <stop offset="1" stop-color="#2a2827"/>
        </linearGradient>
        <linearGradient id="photo-base" x1="0" y1="1" x2="1" y2="0">
          <stop offset="0" stop-color="#d9c7bd"/>
          <stop offset="0.3" stop-color="#7c5f55"/>
          <stop offset="0.55" stop-color="#1c1513"/>
          <stop offset="0.8" stop-color="#3a302c"/>
          <stop offset="1" stop-color="#8b857f"/>
        </linearGradient>
        <radialGradient id="photo-glow" cx="0.3" cy="0.72" r="0.4">
          <stop offset="0" stop-color="rgba(255,236,228,0.85)"/>
          <stop offset="1" stop-color="rgba(255,236,228,0)"/>
        </radialGradient>
        <radialGradient id="photo-shadow" cx="0.72" cy="0.45" r="0.38">
          <stop offset="0" stop-color="rgba(8,6,5,0.9)"/>
          <stop offset="1" stop-color="rgba(8,6,5,0)"/>
        </radialGradient>
        <clipPath id="photo-clip">
          <circle cx="900" cy="950" r="450"/>
        </clipPath>
      </defs>

      <rect x="0" y="0" width="1200" height="1200" fill="url(#backdrop-tone)"
            role="img" aria-label="Dim photograph of grand piano keys fading into shadow"/>

      <text x="762" y="425" font-family="Raleway, sans-serif" font-weight="800"
            font-size="600" fill="var(--numeral)">3</text>

      <path d="M 355 375 C 362 445 420 472 520 462" fill="none" stroke="rgba(120,120,120,0.3)" stroke-width="26"/>

      <circle cx="900" cy="950" r="530" fill="none" stroke="var(--ring)" stroke-width="2"/>
      <g clip-path="url(#photo-clip)" role="img" aria-label="Backlit photograph of a pianist's hand playing wedding music on piano keys">
        <rect x="450" y="500" width="900" height="900" fill="url(#photo-base)"/>
        <rect x="450" y="500" width="900" height="900" fill="url(#photo-shadow)"/>
        <rect x="450" y="500" width="900" height="900" fill="url(#photo-glow)"/>
      </g>
      <circle cx="900" cy="950" r="450" fill="none" stroke="rgba(170,170,170,0.45)" stroke-width="2"/>
    </svg>

    <div class="frame"></div>

    <p class="volume-label">Volume</p>
    <h1 class="artist-name">Leon Harwick</h1>
    <h2 class="album-title">Timeless Keys for Vows and<br>Banquet Evenings</h2>
  </div>
</body>
</html>
```